Create Oceanfront SEO Website – Marlow Haven

I am web developer to build a high-quality, SEO-optimized website. The site is fully structured with content, layout, and purpose clearly defined, and comes with keyword-rich SEO guidance to maximize search engine visibility. Domain names and page content are provided.

Developer Role:
Build a responsive, fast-loading website in WordPress, allowing us to edit and update content in the future.
Implement SEO best practices, including meta tags, structured data, and optimized content.
Ensure smooth navigation, intuitive UX, and visually appealing design.
Establish the website to a fully functional state, after which we will handle ongoing updates and changes.
Domain and website will be hosted by hostwren under my profile.
Key Highlights:
Structured website with ready-to-use content.
SEO-focused pages for maximum visibility.
Domains and site structure already defined.
Creative freedom in design within the provided framework.

Target Market(s)

vacationers

Industry/Entity Type

vacation and travel

Coding

Coded - Design and coding required

Colors
0054AA
0677BA
7BADD7
CADEEF
E8F1F8
0094D4
00A9DD
6FCCEA
C7EBF8
E9F6FB
00AB8E
00BBA5
67D7C9
C6EFE9
E9F9F6
FFF300
FFF600
FEFA6F
FFFEC7
FFFEE8

Requirements
Must have
• see brief

```html
<!DOCTYPE html>
<html lang="en">
<head>
<meta charset="utf-8">
<title>Book Our Marlow Haven Oceanfront Condo</title>
<link href="https://fonts.googleapis.com/css2?family=Gilda+Display&family=Jost:wght@300;400&display=swap" rel="stylesheet">
<style>
:root{
  --ink:#0054aa;
  --text:#4a5a6a;
  --accent:#0677ba;
  --teal:#00ab8e;
  --teal-soft:#e9f9f6;
  --sky:#e9f6fb;
  --sky-line:#cadeef;
  --sun:#fff300;
  --sun-soft:#fffee8;
  --white:#ffffff;
  --quote:#c7ebf8;
  --badge-a:#00a9dd;
  --badge-b:#00bba5;
  --badge-c:#0054aa;
}
*{box-sizing:border-box;margin:0;padding:0}
html,body{width:1200px;height:3237px;overflow:hidden}
body{background:var(--white);font-family:"Jost",sans-serif;font-weight:300;color:var(--text);position:relative}
.serif{font-family:"Gilda Display",serif;font-weight:400;color:var(--ink)}
section,header{position:absolute;left:0;width:1200px}

/* nav */
.site-nav{top:0;height:50px;background:var(--white);border-bottom:1px solid var(--sky-line)}
.site-nav a{position:absolute;top:21px;font-size:12px;color:#2d3b4a;text-decoration:none;font-weight:400}
.site-nav a.active{color:var(--accent)}
.nav-badge{position:absolute;top:19px;width:19px;height:19px;border-radius:3px}

/* hero */
.hero{top:50px;height:300px;background:var(--sky);text-align:center;border-bottom:3px solid var(--sun)}
.hero h1{position:absolute;left:0;width:1200px;top:60px;font-size:35px;line-height:41px}
.hero p{position:absolute;left:325px;width:550px;top:152px;font-size:10.5px;line-height:17px}
.listing{position:absolute;top:215px;width:75px;height:24px;border-radius:3px;color:#fff;font-size:11px;font-weight:400;line-height:24px;text-align:center}

/* split sections */
.split{background:var(--white)}
.photo{position:absolute;border-radius:2px}
.eyebrow{position:absolute;font-size:10.5px;color:var(--teal);font-weight:400;display:flex;align-items:center;gap:8px}
.eyebrow::before{content:"";width:22px;height:1px;background:var(--teal)}
.eyebrow.center::after{content:"";width:22px;height:1px;background:var(--teal)}
.split h2{position:absolute;left:584px;font-size:26px;line-height:32px}
.split p.body{position:absolute;left:584px;width:395px;font-size:10px;line-height:16.9px}
.thumb{position:absolute;width:122px;height:90px;border-radius:2px}
.more{position:absolute;left:584px;font-size:10.5px;color:var(--accent);font-weight:400;padding:0 3px 4px;border-bottom:1px solid var(--accent)}

/* amenities */
.amenities{top:808px;height:593px;background:var(--teal-soft)}
.center-h{position:absolute;left:0;width:1200px;text-align:center}
.card{position:absolute;width:259px;height:166px;background:var(--white);border:1px solid var(--sky-line);border-radius:3px;text-align:center}
.card svg{position:absolute;left:109px;top:22px;color:var(--accent)}
.card h3{position:absolute;left:0;width:100%;top:70px;font-size:15.5px}
.card p{position:absolute;left:18px;right:18px;top:94px;font-size:10px;line-height:16.9px}

/* gallery */
.gallery{top:1860px;height:477px;background:var(--sun-soft)}
.gallery .tile{position:absolute;width:191px;height:159px}

/* faq */
.faq-item{position:absolute;left:584px;width:395px;height:39px;border-bottom:1px solid var(--sky-line);font-family:"Gilda Display",serif;font-size:11px;color:#1e3550;line-height:20px}
.faq-item svg{position:absolute;right:0;top:6px;color:var(--accent)}

/* testimonials */
.reviews{top:2796px;height:441px;background:var(--sky)}
.review{position:absolute;top:184px;width:259px;height:194px;background:var(--white);border:1px solid var(--sky-line);border-top:3px solid var(--sun);border-radius:3px}
.stars{position:absolute;left:19px;top:16px;color:var(--teal);font-size:15px;letter-spacing:1px}
.review p{position:absolute;left:19px;right:22px;top:46px;font-size:10px;line-height:16.9px}
.review .who{position:absolute;left:19px;top:156px;font-size:10px;color:#3d4d5e}
.review .quote{position:absolute;right:12px;top:146px;font-family:"Gilda Display",serif;font-size:54px;line-height:40px;color:var(--quote)}
</style>
</head>
<body>

<header class="site-nav">
  <a style="left:63px">Home</a>
  <a class="active" style="left:122px">Booking</a>
  <a style="left:191px">About</a>
  <a style="left:249px">Things To Do</a>
  <a style="left:342px">Attractions</a>
  <a style="left:422px">Events &amp; Festivals</a>
  <a style="left:535px">Plan Your Trip</a>
  <a style="left:631px">Local Services</a>
  <a style="left:729px">Nearby Destinations</a>
  <a style="left:1000px">Book Now</a>
  <span class="nav-badge" style="left:1059px;background:var(--badge-a)"></span>
  <span class="nav-badge" style="left:1088px;background:var(--badge-b)"></span>
  <span class="nav-badge" style="left:1117px;background:var(--badge-c)"></span>
</header>

<section class="hero">
  <h1 class="serif">Book Our Marlow Haven<br>Oceanfront Condo</h1>
  <p>Experience the ultimate Marlow Haven getaway in our fully furnished oceanfront condo. Whether you're planning a short vacation, a family trip, or a long-term stay, our condo offers comfort, convenience, and stunning Atlantic views.</p>
  <span class="listing" style="left:475px;background:var(--badge-a)">StayNest</span>
  <span class="listing" style="left:562px;background:var(--badge-b)">LeaseLoft</span>
  <span class="listing" style="left:650px;background:var(--badge-c)">HomeHarbor</span>
</section>

<section class="split" style="top:353px;height:455px">
  <div class="photo" role="img" aria-label="Condo courtyard with a kidney-shaped pool, palm trees and a mint two-storey building" style="left:221px;top:57px;width:303px;height:338px;background:linear-gradient(180deg,#8fc2ea 0%,#d8eef6 30%,#8fd3c8 55%,#3fc2d8 75%,#b9aea2 100%)"></div>
  <div class="eyebrow" style="left:584px;top:58px">Key Highlights</div>
  <h2 class="serif" style="top:80px">5-Star Oceanfront Experience</h2>
  <p class="body" style="top:121px">Our Marlow Haven condo delivers an unmatched vacation experience by providing the space and comfort of home directly on the Atlantic shoreline. You'll enjoy the luxury of a private, furnished balcony with panoramic ocean views, the convenience of a fully equipped kitchen, and the peace of mind knowing your entire family—including your dog—is welcome thanks to our pet-friendly policy. Combined with free parking and the ease of walking to local shops and the beach, our rental ensures your Florida getaway is stress-free, comfortable, and truly unforgettable.</p>
  <div class="thumb" role="img" aria-label="Bedroom with white bedding" style="left:584px;top:259px;background:linear-gradient(180deg,#c9c6c1,#e6e3df)"></div>
  <div class="thumb" role="img" aria-label="Living room with sofa and TV" style="left:720px;top:259px;background:linear-gradient(180deg,#c4c1bc,#d9d2c6)"></div>
  <div class="thumb" role="img" aria-label="Kitchen with white cabinets" style="left:857px;top:259px;background:linear-gradient(180deg,#c8c5c0,#b9ab98)"></div>
  <div class="more" style="top:372px">Learn More About Our Rental →</div>
</section>

<section class="amenities">
  <div class="eyebrow center" style="left:523px;top:61px">Featured Amenities</div>
  <h2 class="serif center-h" style="top:82px;font-size:27px">All the Comforts of Home</h2>
  <p class="center-h" style="top:121px;left:380px;width:440px;font-size:10px;line-height:17px">From your private, oceanfront balcony to the fully equipped kitchen, our Marlow Haven condo is designed for maximum relaxation and convenience. Discover our essential amenities.</p>

  <div class="card" style="left:195px;top:185px">
    <svg width="40" height="34" viewBox="0 0 40 34" fill="none" stroke="currentColor" stroke-width="1.2"><rect x="2" y="2" width="36" height="30"/><rect x="7" y="6" width="26" height="18"/><path d="M2 26h36M6 26v6M12 26v6M18 26v6M24 26v6M30 26v6M34 26v6"/></svg>
    <h3 class="serif">Oceanfront Balcony</h3>
    <p>Step out onto your private, furnished balcony and breathe in the salt air while enjoying panoramic Atlantic views as far as the eye can see.</p>
  </div>
  <div class="card" style="left:470px;top:185px">
    <svg width="40" height="34" viewBox="0 0 40 34" fill="none" stroke="currentColor" stroke-width="1.2"><path d="M6 12 Q18 0 32 8 Z"/><path d="M19 6 L14 28"/><path d="M2 26 Q8 22 14 26 T26 26 T38 26M2 31 Q8 27 14 31 T26 31 T38 31"/><circle cx="34" cy="4" r="2.5"/></svg>
    <h3 class="serif">Direct Beach Access</h3>
    <p>Enjoy the ultimate coastal convenience with our direct beach access, placing you just steps away from the shimmering Marlow Haven shoreline.</p>
  </div>
  <div class="card" style="left:745px;top:185px">
    <svg width="40" height="34" viewBox="0 0 40 34" fill="none" stroke="currentColor" stroke-width="1.2"><path d="M10 4v18M18 4v18M10 9h8M10 15h8"/><path d="M2 22 Q8 18 14 22 T26 22 T38 22M2 28 Q8 24 14 28 T26 28 T38 28"/><circle cx="31" cy="6" r="3"/></svg>
    <h3 class="serif">Private Pool</h3>
    <p>Take a refreshing dip in the pool, the perfect spot to cool off and relax after spending time on the Marlow Haven sand.</p>
  </div>
  <div class="card" style="left:195px;top:367px">
    <svg width="40" height="34" viewBox="0 0 40 34" fill="none" stroke="currentColor" stroke-width="1.2"><path d="M20 30 C6 20 4 12 10 8 C14 5 18 8 20 12 C22 8 26 5 30 8 C36 12 34 20 20 30 Z"/><path d="M2 32h36"/></svg>
    <h3 class="serif">Pet-Friendly</h3>
    <p>Bring your beloved companion along for the vacation—our pet-friendly accommodations ensure they also enjoy the Marlow Haven getaway.</p>
  </div>
  <div class="card" style="left:470px;top:367px">
    <svg width="40" height="34" viewBox="0 0 40 34" fill="none" stroke="currentColor" stroke-width="1.2"><rect x="8" y="2" width="24" height="9"/><path d="M16 2v9M24 2v9"/><rect x="4" y="16" width="32" height="12" rx="2"/><path d="M8 16v-2h24v2M8 28v4M32 28v4M4 22h32"/></svg>
    <h3 class="serif">Spacious Living Area</h3>
    <p>Relax and spread out in our spacious living area, featuring comfortable seating and ocean views, making it the perfect spot for family time.</p>
  </div>
  <div class="card" style="left:745px;top:367px">
    <svg width="40" height="34" viewBox="0 0 40 34" fill="none" stroke="currentColor" stroke-width="1.2"><rect x="2" y="12" width="22" height="20"/><path d="M2 20h22M8 16h10"/><rect x="26" y="8" width="12" height="24"/><path d="M26 18h12M10 4h8v6h-8z"/></svg>
    <h3 class="serif">Fully Furnished</h3>
    <p>You'll find everything you need for a comfortable stay, complete with a well-equipped kitchen, linens, and all the essentials of home.</p>
  </div>
</section>

<section class="split" style="top:1401px;height:459px">
  <div class="photo" role="img" aria-label="Aerial view of the condo buildings, parking and the ocean beyond" style="left:221px;top:60px;width:303px;height:338px;background:linear-gradient(180deg,#2f8fb0 0%,#62b3c4 18%,#d9cfbf 30%,#8a8d86 55%,#b8a88e 75%,#5f6a5c 100%)"></div>
  <div class="eyebrow" style="left:584px;top:62px">More Than a Rental</div>
  <h2 class="serif" style="top:84px">Marlow Haven Dream Vacation</h2>
  <p class="body" style="top:125px">Our oceanfront condo is the absolute best choice for your getaway, seamlessly blending the natural beauty of the Atlantic coast with premium comforts. Imagine waking up to panoramic ocean views from your private balcony, enjoying direct, steps-from-the-sand access for morning walks, and having a spacious, pet-friendly home base complete with a fully equipped kitchen. We offer the perfect, effortless escape where every detail, from the free parking to the easy booking, is designed so you can focus entirely on making unforgettable memories.</p>
  <div class="thumb" role="img" aria-label="Aerial view of the pool" style="left:584px;top:263px;background:linear-gradient(135deg,#6d7a66,#4fc3d6,#7d8a72)"></div>
  <div class="thumb" role="img" aria-label="Beach umbrella and loungers by turquoise water" style="left:720px;top:263px;background:linear-gradient(180deg,#8fd0ef,#4bc6d6 50%,#f1ead9)"></div>
  <div class="thumb" role="img" aria-label="Beachside dining under umbrellas" style="left:857px;top:263px;background:linear-gradient(180deg,#3f7fc4,#e9d49a 45%,#f2f1ec)"></div>
  <div class="more" style="top:377px">Learn More About Marlow Haven →</div>
</section>

<section class="gallery">
  <div class="tile" role="img" aria-label="Living room with sofa and ceiling fan" style="left:195px;top:60px;background:linear-gradient(180deg,#c2bfba,#d2c4ab)"></div>
  <div class="tile" role="img" aria-label="Kitchen with white cabinets and dark fridge" style="left:401px;top:60px;background:linear-gradient(180deg,#cac7c2,#e0ddd8)"></div>
  <div class="tile" role="img" aria-label="Kitchen and dining area" style="left:607px;top:60px;background:linear-gradient(180deg,#c5c2bd,#b7b2a8)"></div>
  <div class="tile" role="img" aria-label="Living and dining area" style="left:813px;top:60px;background:linear-gradient(180deg,#c0bdb8,#cbbfaa)"></div>
  <div class="tile" role="img" aria-label="Living room with TV cabinet" style="left:195px;top:233px;background:linear-gradient(180deg,#c6c3be,#a88f74)"></div>
  <div class="tile" role="img" aria-label="Bedroom with window" style="left:401px;top:233px;background:linear-gradient(180deg,#bfbcb7,#e9e6e1)"></div>
  <div class="tile" role="img" aria-label="Hallway toward the bathroom" style="left:607px;top:233px;background:linear-gradient(180deg,#c9c6c1,#d8d5d0)"></div>
  <div class="tile" role="img" aria-label="Bathroom with vanity lights" style="left:813px;top:233px;background:linear-gradient(180deg,#cfccc7,#ebe9e6)"></div>
</section>

<section class="split" style="top:2337px;height:459px">
  <div class="photo" role="img" aria-label="Laundry room with washer, dryer and beach gear" style="left:221px;top:60px;width:303px;height:338px;background:linear-gradient(180deg,#c79b66 0%,#d7c2a4 22%,#e7e6e3 45%,#f3f2f0 70%,#a9a8a5 100%)"></div>
  <div class="eyebrow" style="left:584px;top:65px">FAQs</div>
  <h2 class="serif" style="top:83px;font-size:27px;line-height:34px">Questions? We've Got Answers!</h2>
  <p class="body" style="top:127px">Check out our most common questions regarding check-in, pet approvals, location details, and the best ways to book our oceanfront condo.</p>
  <div class="faq-item" style="top:177px">Q: What is the maximum number of guests<svg width="10" height="8" viewBox="0 0 10 8" fill="none" stroke="currentColor" stroke-width="1.2"><path d="M1 2l4 4 4-4"/></svg></div>
  <div class="faq-item" style="top:216px">Q: Is the condo pet-friendly?<svg width="10" height="8" viewBox="0 0 10 8" fill="none" stroke="currentColor" stroke-width="1.2"><path d="M1 2l4 4 4-4"/></svg></div>
  <div class="faq-item" style="top:255px">Q: How far is the condo from the beach?<svg width="10" height="8" viewBox="0 0 10 8" fill="none" stroke="currentColor" stroke-width="1.2"><path d="M1 2l4 4 4-4"/></svg></div>
  <div class="faq-item" style="top:294px">Q: Can I book directly on StayNest, HomeHarbor, or LeaseLoft?<svg width="10" height="8" viewBox="0 0 10 8" fill="none" stroke="currentColor" stroke-width="1.2"><path d="M1 2l4 4 4-4"/></svg></div>
  <div class="faq-item" style="top:333px;border-bottom:none">Q: Are there family-friendly activities nearby?<svg width="10" height="8" viewBox="0 0 10 8" fill="none" stroke="currentColor" stroke-width="1.2"><path d="M1 2l4 4 4-4"/></svg></div>
  <div class="more" style="top:377px">View More Frequently Asked Questions →</div>
</section>

<section class="reviews">
  <div class="eyebrow center" style="left:540px;top:59px">Testimonials</div>
  <h2 class="serif center-h" style="top:79px;font-size:27px">Real Stays. Real Memories.</h2>
  <p class="center-h" style="top:121px;left:380px;width:440px;font-size:10px;line-height:17px">These verified reviews cover everything from the ease of beach access to the quality of the accommodations and the convenience of booking through StayNest, LeaseLoft, and HomeHarbor.</p>

  <div class="review" style="left:195px">
    <div class="stars">★★★★★</div>
    <p>"The view from this condo is absolutely unbeatable! Watching the sunrise over the Atlantic from the balcony was the highlight of our trip. It truly is steps from the sand, making our beach days effortless. The condo itself was clean, modern, and perfect. We'll be back!"</p>
    <div class="who">Dana R. — Booked On StayNest</div>
    <div class="quote">”</div>
  </div>
  <div class="review" style="left:470px">
    <div class="stars">★★★★★</div>
    <p>"Excellent communication and a smooth booking process through LeaseLoft! The condo had everything we needed—a fully equipped kitchen, fast Wi-Fi, and great air conditioning. It was a relaxing, quiet, and very secure building. A fantastic experience with ocean views!"</p>
    <div class="who">Owen P. — Booked On LeaseLoft</div>
    <div class="quote">”</div>
  </div>
  <div class="review" style="left:745px">
    <div class="stars">★★★★★</div>
    <p>"We finally found the perfect Florida getaway where we could bring our dog! Being pet-friendly was huge, and the easy access to the designated dog walking beach areas was a lifesaver. The condo felt spacious and cozy—a true home away from home."</p>
    <div class="who">The Whitfield Family — Booked On HomeHarbor</div>
    <div class="quote">”</div>
  </div>
</section>

</body>
</html>
```